Steady Valve Systems

I need a business card with the attached logo.
The second page I have attached is what we are looking for. We want doubles sided. We would like the blues fading and the logo on the back.

Industry/Entity Type

Business

```html
<!DOCTYPE html>
<html lang="en">
<head>
<meta charset="utf-8">
<title>Steady Valve Systems – Business Card</title>
<link rel="stylesheet" href="https://fonts.googleapis.com/css2?family=Cinzel:wght@400;600;700&display=swap">
<style>
  :root {
    --stage: #e9eaec;
    --brand-blue: #0a5aa6;
    --brand-blue-deep: #0b4d8f;
    --brand-blue-light: #1d6fbf;
    --ink-navy: #0c2f6b;
    --card-white: #ffffff;
    --card-grey: #e4e4e4;
  }
  * { box-sizing: border-box; margin: 0; padding: 0; }
  html, body {
    width: 1200px;
    height: 1000px;
    overflow: hidden;
    background: var(--stage);
    font-family: "Cinzel", serif;
  }
  .stage {
    position: relative;
    width: 1200px;
    height: 1000px;
  }
  .card {
    position: absolute;
    top: 340px;
    width: 492px;
    height: 302px;
    overflow: hidden;
  }

  /* Front */
  .card--front {
    left: 64px;
    background: linear-gradient(180deg, var(--card-white) 0%, #f1f1f1 100%);
  }
  .front__band {
    position: absolute;
    left: 0; right: 0; bottom: 0;
    height: 120px;
    background: linear-gradient(90deg, var(--brand-blue-deep) 0%, var(--brand-blue) 50%, var(--brand-blue-light) 100%);
  }
  .front__rule {
    position: absolute;
    left: 0; right: 0;
    top: 180px;
    height: 2px;
    background: #c9c9c9;
  }
  .front__wordmark {
    position: absolute;
    left: 0; right: 0;
    top: 92px;
    text-align: center;
    color: var(--brand-blue);
    font-weight: 700;
    line-height: 1;
  }
  .front__wordmark .name-main {
    display: block;
    font-size: 46px;
    letter-spacing: 2px;
  }
  .front__wordmark .name-sub {
    display: block;
    margin-top: 8px;
    font-size: 15px;
    letter-spacing: 3px;
  }

  /* Back */
  .card--back {
    left: 662px;
    background: linear-gradient(90deg, var(--card-grey) 0%, #efefef 45%, var(--card-white) 100%);
  }
  .back__strip {
    position: absolute;
    left: 0; top: 0; bottom: 0;
    width: 33px;
    background: linear-gradient(180deg, var(--brand-blue-light) 0%, var(--brand-blue) 55%, var(--brand-blue-deep) 100%);
  }
  .back__wordmark {
    position: absolute;
    left: 44px;
    top: 36px;
    color: var(--brand-blue);
    font-weight: 700;
    font-size: 17px;
    letter-spacing: 1px;
  }
  .back__person {
    position: absolute;
    right: 20px;
    top: 126px;
    text-align: right;
    color: var(--ink-navy);
  }
  .back__name {
    font-size: 22px;
    font-weight: 400;
    letter-spacing: 1px;
    line-height: 1.1;
  }
  .back__role {
    font-size: 11.5px;
    letter-spacing: 1px;
    margin-top: 2px;
    margin-right: 11px;
  }
  .back__contact {
    position: absolute;
    left: 45px;
    top: 216px;
    color: var(--ink-navy);
    font-size: 11.5px;
    letter-spacing: 1px;
    line-height: 18px;
    list-style: none;
  }
</style>
</head>
<body>
<main class="stage">
  <section class="card card--front" aria-label="Card front">
    <div class="front__band"></div>
    <div class="front__rule"></div>
    <h1 class="front__wordmark">
      <span class="name-main">STEADY VALVE</span>
      <span class="name-sub">SYSTEMS</span>
    </h1>
  </section>

  <section class="card card--back" aria-label="Card back">
    <div class="back__strip"></div>
    <div class="back__wordmark">STEADY VALVE</div>
    <div class="back__person">
      <p class="back__name">Martin ELLERY</p>
      <p class="back__role">Sales &amp; Service - North Dakota</p>
    </div>
    <ul class="back__contact">
      <li>mellery@steadyvalve.com</li>
      <li>Cell: 555.210.0483</li>
      <li>Office: 555.318.2207</li>
    </ul>
  </section>
</main>
</body>
</html>
```